New corporate e-mail signature

We need a new e-mail signature for our company that is clean and professional. The requests are attached in a document.

Target Market(s)

CFO, CTO, Controllers, leaders, decision-makers.

Industry/Entity Type

Information Technology

Colors

Designer to choose colors to be used in the design.

Requirements
Must have
• See the PowerPoint document.
• - keep it as simple as possible.
• - same style as our new website design
• - It has to look good in all e-mail readers, and on all surfaces.
Nice to have
• - Please also attach 'best practise' for how to use the signature.
Should not have
• See the PowerPoint document. Use our color palette.
• - Do not include photo!

```html
<!DOCTYPE html>
<html lang="en">
<head>
<meta charset="utf-8">
<title>Ledgerline e-mail signature</title>
<link rel="stylesheet" href="https://fonts.googleapis.com/css2?family=Open+Sans:wght@300;400;600;700;800&display=swap">
<style>
  :root {
    --navy: #0d3b6f;
    --ink: #1a1a1a;
    --grey: #4a4a4a;
    --accent-bar: #2f3f8e;
    --label-blue: #3a8fd4;
    --sky-dark: #1d3f7a;
    --sky-mid: #4f7fc4;
    --sky-light: #c9d9ee;
    --social-1: #2aa3e6;
    --social-2: #3b5a9a;
    --social-3: #1b76b4;
    --paper: #ffffff;
  }
  html, body {
    margin: 0;
    padding: 0;
    overflow: hidden;
    background: var(--paper);
  }
  .signature {
    position: relative;
    width: 1200px;
    height: 323px;
    overflow: hidden;
    background: var(--paper);
    font-family: "Open Sans", Arial, sans-serif;
  }
  .hero-band {
    position: absolute;
    left: 0;
    top: 0;
    width: 1200px;
    height: 117px;
    background:
      radial-gradient(ellipse 260px 90px at 620px 45px, rgba(255,255,255,0.75), rgba(255,255,255,0) 70%),
      linear-gradient(100deg, var(--sky-dark) 0%, var(--sky-mid) 30%, var(--sky-light) 50%, var(--sky-mid) 72%, var(--sky-dark) 100%);
  }
  .identity {
    position: absolute;
    right: 802px;
    top: 148px;
    text-align: right;
  }
  .identity__name {
    margin: 0;
    font-size: 64px;
    font-weight: 700;
    line-height: 64px;
    letter-spacing: 1px;
    color: var(--navy);
  }
  .identity__role {
    margin: 6px 0 0;
    font-size: 26px;
    font-weight: 400;
    line-height: 30px;
    color: var(--ink);
  }
  .identity__company {
    margin: 4px 0 0;
    font-size: 30px;
    font-weight: 800;
    line-height: 32px;
    color: var(--grey);
  }
  .divider {
    position: absolute;
    left: 444px;
    top: 154px;
    width: 4px;
    height: 138px;
    background: var(--accent-bar);
  }
  .contact {
    position: absolute;
    left: 472px;
    top: 158px;
    margin: 0;
    padding: 0;
    list-style: none;
  }
  .contact__row {
    display: flex;
    height: 34.5px;
    align-items: center;
  }
  .contact__label {
    width: 46px;
    font-size: 19px;
    font-weight: 300;
    color: var(--label-blue);
  }
  .contact__value {
    font-size: 21px;
    font-weight: 400;
    color: var(--ink);
  }
  .social {
    position: absolute;
    right: 32px;
    top: 154px;
    margin: 0;
    padding: 0;
    list-style: none;
  }
  .social__item {
    display: flex;
    justify-content: flex-end;
    align-items: center;
    gap: 8px;
    height: 38px;
    margin-bottom: 8px;
    font-size: 13px;
    font-weight: 600;
    color: var(--grey);
  }
  .social__mark {
    width: 38px;
    height: 38px;
  }
  .social__mark--flock { background: var(--social-1); border-radius: 50%; }
  .social__mark--kinbook { background: var(--social-2); }
  .social__mark--workline { background: var(--social-3); }
</style>
</head>
<body>
  <div class="signature">
    <div class="hero-band" role="img" aria-label="Photo of glass office buildings against a blue sky with clouds"></div>

    <div class="identity">
      <h1 class="identity__name">JOHN DOE</h1>
      <p class="identity__role">MANAGING DIRECTOR</p>
      <p class="identity__company">ledgerline</p>
    </div>

    <div class="divider"></div>

    <ul class="contact">
      <li class="contact__row"><span class="contact__label">E:</span><span class="contact__value">johndoe@ledgerline.com</span></li>
      <li class="contact__row"><span class="contact__label">T:</span><span class="contact__value">+1 (555) 010 2040</span></li>
      <li class="contact__row"><span class="contact__label">w:</span><span class="contact__value">www.ledgerline.com</span></li>
      <li class="contact__row"><span class="contact__label">L:</span><span class="contact__value">Solbergveien 18 1366 LYSAKER</span></li>
    </ul>

    <ul class="social">
      <li class="social__item">Flock<span class="social__mark social__mark--flock"></span></li>
      <li class="social__item">Kinbook<span class="social__mark social__mark--kinbook"></span></li>
      <li class="social__item">Workline<span class="social__mark social__mark--workline"></span></li>
    </ul>
  </div>
</body>
</html>
```